Cool modern, tech Business card design

Looking for a new business card design for our Managed IT Services company. We would like 2 sides, with the logo one one side horizontally and then the information on the back in either vertical or horizontal. We want our colors from the logo incorporated but also would like to see the color gray in there as well.

Target Market(s)

IT, Information Technology, Tech, Service

Industry/Entity Type

It Service

Contact Information for Business Card

Carl Penner
Managing Partner
(P)555-271-4830 ext xxx
(F)555-271-4831
www.brixtelcore.com

Font styles to use
Sans Serif

Colors
959595
000000
ec1f27

Requirements
Must have
• Logo on one side with some nice design or pattern
• Information on back in either vertical or horizontal format
Nice to have
• For it to look cool, tech, modern, stand out.

```html
<!DOCTYPE html>
<html lang="en">
<head>
<meta charset="utf-8">
<title>Brixtelcore Business Card</title>
<link href="https://fonts.googleapis.com/css2?family=Montserrat:ital,wght@0,400;0,500;0,700;1,400&display=swap" rel="stylesheet">
<style>
  :root {
    --red: #c8102e;
    --red-bright: #ec1f27;
    --ink: #231f20;
    --charcoal: #333333;
    --charcoal-deep: #262626;
    --paper: #eeeeee;
    --grey: #959595;
    --white: #ffffff;
  }
  * { margin: 0; padding: 0; box-sizing: border-box; }
  html, body { width: 1200px; height: 1000px; overflow: hidden; background: var(--white); }
  body { position: relative; font-family: "Montserrat", sans-serif; }

  .card {
    position: absolute;
    left: 274px;
    width: 652px;
    height: 373px;
    overflow: hidden;
    box-shadow: 0 18px 40px rgba(0, 0, 0, 0.18);
  }
  .card--front { top: 90px; }
  .card--back { top: 537px; height: 372px; }
  .card__art { position: absolute; inset: 0; width: 100%; height: 100%; }

  .wordmark {
    position: absolute;
    display: flex;
    align-items: center;
    gap: 8px;
    color: var(--ink);
    font-weight: 500;
    letter-spacing: -0.5px;
  }
  .wordmark__square { background: var(--red); display: block; }
  .card--front .wordmark { left: 32px; top: 196px; font-size: 25px; }
  .card--front .wordmark__square { width: 12px; height: 12px; }
  .card--back .wordmark { left: 0; right: 0; top: 152px; justify-content: center; font-size: 46px; gap: 12px; }
  .card--back .wordmark__square { width: 20px; height: 20px; }

  .name {
    position: absolute;
    left: 276px;
    top: 80px;
    color: #f1f1f1;
    font-size: 49px;
    font-weight: 700;
    letter-spacing: 0.3px;
  }
  .role {
    position: absolute;
    left: 274px;
    top: 150px;
    color: #f1f1f1;
    font-size: 21px;
    font-style: italic;
    font-weight: 400;
  }
  .contact {
    position: absolute;
    left: 354px;
    top: 253px;
    color: var(--white);
    font-size: 13px;
    line-height: 14px;
  }
  .contact__label { color: var(--red-bright); font-weight: 700; }
  .contact__ext { color: var(--red-bright); }
  .website {
    position: absolute;
    left: 0; right: 0;
    top: 322px;
    text-align: center;
    color: #d8d8d8;
    font-size: 12.5px;
    letter-spacing: 0.3px;
  }
</style>
</head>
<body>

<section class="card card--front" aria-label="Business card front">
  <svg class="card__art" viewBox="0 0 652 373" aria-hidden="true">
    <defs>
      <linearGradient id="front-paper" x1="0" y1="0" x2="1" y2="1">
        <stop offset="0" stop-color="#f3f3f3"/>
        <stop offset="1" stop-color="#e6e6e6"/>
      </linearGradient>
      <linearGradient id="front-dark" x1="0" y1="0" x2="0" y2="1">
        <stop offset="0" stop-color="#2f2f2f"/>
        <stop offset="1" stop-color="#404040"/>
      </linearGradient>
      <linearGradient id="edge-red" x1="0" y1="0" x2="0" y2="1">
        <stop offset="0" stop-color="#d31830"/>
        <stop offset="1" stop-color="#7d0a1c"/>
      </linearGradient>
    </defs>
    <rect class="paper" width="652" height="373" fill="url(#front-paper)"/>
    <polygon class="facet" points="40,0 250,0 236,95 150,60" fill="rgba(214,70,95,0.22)"/>
    <polygon class="facet" points="90,0 200,0 228,118 185,100" fill="rgba(214,70,95,0.18)"/>
    <polygon class="facet" points="212,18 240,0 226,105 188,90" fill="rgba(220,60,85,0.45)"/>
    <polygon class="facet" points="0,250 170,330 205,373 0,373" fill="rgba(214,70,95,0.22)"/>
    <polygon class="facet" points="30,300 160,320 190,373 20,373" fill="rgba(214,70,95,0.2)"/>
    <polygon class="corner" points="0,290 42,318 18,373 0,373" fill="var(--red)"/>
    <polygon class="corner" points="12,300 44,318 28,355" fill="rgba(240,150,165,0.55)"/>
    <polygon class="dark-panel" points="251,0 652,0 652,373 201,373" fill="url(#front-dark)"/>
    <polygon class="accent" points="232,0 252,0 246,60" fill="var(--red)"/>
    <polygon class="edge" points="640,0 652,0 652,373 620,373" fill="url(#edge-red)"/>
    <rect class="name-band" x="223" y="72" width="396" height="114" fill="var(--red)"/>
    <line x1="241" y1="142" x2="597" y2="142" stroke="#f1f1f1" stroke-width="1.5"/>
    <line x1="170" y1="267" x2="290" y2="267" stroke="var(--red)" stroke-width="1.5"/>
    <line x1="538" y1="267" x2="588" y2="267" stroke="var(--red)" stroke-width="1.5"/>
    <circle cx="329" cy="267" r="14" fill="var(--red)"/>
    <path class="phone-icon" d="M323 258 c1.5-1 3-1 3.5 0.5 l1.6 3.4 c0.4 0.9 0 1.8-0.8 2.3 l-1 0.6 c0.9 2.2 2.4 4 4.5 5.2 l0.8-1 c0.6-0.7 1.5-0.9 2.3-0.4 l3.1 2 c1.2 0.8 1.1 2.3 0 3.4 c-1.5 1.5-3.8 1.9-5.8 0.8 c-4.6-2.5-7.9-6.8-9.4-11.8 c-0.6-2-0.1-3.8 1.2-5 z" fill="var(--white)"/>
  </svg>

  <div class="wordmark"><span class="wordmark__name">brixtelcore</span><span class="wordmark__square"></span></div>
  <h1 class="name">Carl Penner</h1>
  <p class="role">Managing Partner</p>
  <p class="contact">
    <span class="contact__label">P</span> 555 271 4830 <span class="contact__ext">ext</span> xxx<br>
    <span class="contact__label">F</span> 555 271 4831
  </p>
</section>

<section class="card card--back" aria-label="Business card back">
  <svg class="card__art" viewBox="0 0 652 372" aria-hidden="true">
    <defs>
      <radialGradient id="back-paper" cx="0.5" cy="0.35" r="0.7">
        <stop offset="0" stop-color="#f4f4f4"/>
        <stop offset="1" stop-color="#dcdcdc"/>
      </radialGradient>
    </defs>
    <rect class="paper" width="652" height="372" fill="url(#back-paper)"/>
    <g class="side-facets">
      <polygon points="0,0 30,0 178,298 0,298" fill="rgba(214,70,95,0.28)"/>
      <polygon points="0,40 92,140 132,298 0,298" fill="rgba(214,70,95,0.18)"/>
      <polygon points="20,262 112,214 160,298 40,298" fill="rgba(255,255,255,0.35)"/>
      <line x1="88" y1="104" x2="156" y2="250" stroke="var(--red)" stroke-width="4"/>
      <line x1="175" y1="64" x2="128" y2="164" stroke="rgba(255,255,255,0.8)" stroke-width="2.5"/>
    </g>
    <g class="side-facets" transform="translate(652 0) scale(-1 1)">
      <polygon points="0,0 30,0 178,298 0,298" fill="rgba(214,70,95,0.28)"/>
      <polygon points="0,40 92,140 132,298 0,298" fill="rgba(214,70,95,0.18)"/>
      <polygon points="20,262 112,214 160,298 40,298" fill="rgba(255,255,255,0.35)"/>
      <line x1="88" y1="104" x2="156" y2="250" stroke="var(--red)" stroke-width="4"/>
      <line x1="175" y1="64" x2="128" y2="164" stroke="rgba(255,255,255,0.8)" stroke-width="2.5"/>
    </g>
    <rect class="footer-band" x="0" y="298" width="652" height="74" fill="var(--charcoal-deep)"/>
    <polygon class="corner" points="0,280 72,252 110,316 0,316" fill="var(--red)"/>
    <polygon class="corner" points="22,272 72,252 96,292" fill="rgba(240,140,160,0.55)"/>
    <polygon class="corner" points="652,280 580,252 542,316 652,316" fill="var(--red)"/>
    <polygon class="corner" points="630,272 580,252 556,292" fill="rgba(240,140,160,0.55)"/>
  </svg>

  <div class="wordmark"><span class="wordmark__name">brixtelcore</span><span class="wordmark__square"></span></div>
  <p class="website">www.brixtelcore.com</p>
</section>

</body>
</html>
```